Outdated Brindlequay.com Website redesign

Brindlequay.com is a construction supply company with 90% delivery of their product to local area builders. Phase one is about improving their online presence, mobile-friendly, and being informative. We are not looking to add any e-commerce abilities in this phase. Please review the documents attached for all the details you need to produce a mock-up. We are also redeveloping their logo (here in DC) but for now, use their old logo asa. place holder.

```html
<!DOCTYPE html>
<html lang="en">
<head>
<meta charset="utf-8">
<title>Brindlequay Industries – Construction Supplies</title>
<link href="https://fonts.googleapis.com/css2?family=IBM+Plex+Sans:wght@400;500;600&family=Michroma&display=swap" rel="stylesheet">
<style>
:root{
  --green:#0a8a0a;
  --green-dark:#046404;
  --green-deep:#0b5f10;
  --ink:#111;
  --text:#333;
  --muted:#8a8a8a;
  --line:#d9d9d9;
  --grey-bg:#f4f4f4;
  --star:#f5a000;
  --white:#fff;
  --footer:#0d0d0d;
}
*{box-sizing:border-box;margin:0;padding:0}
html,body{width:1200px;height:3242px;overflow:hidden}
body{position:relative;font-family:"IBM Plex Sans",Arial,sans-serif;color:var(--text);background:var(--white)}
.abs{position:absolute}
.display{font-family:"Michroma","Arial Black",sans-serif;text-transform:uppercase;color:var(--ink);letter-spacing:.5px;font-weight:400}

/* hero */
.hero{left:0;top:0;width:1200px;height:660px;overflow:hidden}
.hero-photo{left:0;top:0;width:1200px;height:660px;background:linear-gradient(180deg,#6c5a45 0%,#9b7c57 35%,#8a8c90 70%,#b9bcbf 100%)}
.hero-shade{left:0;top:0;width:1200px;height:660px;background:rgba(20,20,20,.35)}
.topbar{left:0;top:0;width:1200px;height:85px;background:linear-gradient(90deg,rgba(8,110,8,.85),rgba(8,110,8,.55))}
.brand{display:flex;align-items:center;gap:10px;left:112px;top:26px;color:var(--white);font-weight:600;font-size:20px;letter-spacing:1px}
.brand-dot{width:30px;height:30px;border-radius:50%;background:var(--green);border:2px solid var(--white)}
.contact-item{display:flex;gap:12px;align-items:center;top:14px;color:var(--white)}
.contact-item .label{font-family:"Michroma",sans-serif;font-size:14px;text-transform:uppercase}
.contact-item .value{font-size:16px;font-weight:500;margin-top:6px}
.nav{left:112px;top:85px;width:976px;height:60px;background:var(--white);display:flex;align-items:center;padding:0 26px;font-size:15px;color:var(--ink)}
.nav a{color:var(--ink);text-decoration:none;margin-right:47px}
.nav a.active{color:var(--green)}
.search{margin-left:-8px;width:234px;height:36px;border-radius:18px;background:#ececec;display:flex;align-items:center;justify-content:space-between;padding:0 20px;font-size:14px}
.socials{display:flex;gap:12px;margin-left:38px}
.socials span{width:12px;height:12px;border-radius:50%;background:var(--green)}
.hero-sub{left:0;width:1200px;top:258px;text-align:center;color:var(--white);font-size:21px;font-weight:500}
.hero-title{left:0;width:1200px;top:302px;text-align:center;color:var(--white);font-size:42px;line-height:48px}
.btn{display:inline-flex;align-items:center;justify-content:center;border-radius:30px;font-family:"Michroma",sans-serif;text-transform:uppercase;color:var(--green);background:var(--white)}
.hero-btn{left:502px;top:422px;width:195px;height:55px;font-size:16px}
.dots{left:568px;top:583px;display:flex;gap:8px}
.dots span{width:11px;height:11px;border-radius:50%;background:var(--white)}
.dots span.off{background:transparent;border:1.5px solid var(--white)}

/* why */
.why-kicker{left:112px;top:722px;font-size:18px;font-weight:500;color:var(--ink)}
.why-title{left:112px;top:760px;width:270px;font-size:18px;white-space:nowrap;letter-spacing:0}
.why-text{left:112px;top:800px;width:260px;font-size:15px;line-height:26px}
.learn{left:112px;top:913px;font-family:"Michroma",sans-serif;font-size:15px;color:var(--green);text-transform:uppercase}
.arrows{left:328px;top:913px;display:flex;gap:16px;font-size:15px}
.feature{top:726px;width:250px;height:250px;border-left:1px solid var(--line);padding-left:21px}
.feature h3{font-family:"Michroma",sans-serif;font-size:12px;line-height:24px;color:var(--ink);text-transform:uppercase;font-weight:400;margin-top:12px;letter-spacing:0}
.feature p{font-size:11.5px;line-height:21px;color:var(--muted);margin-top:10px}

/* products */
.products{left:0;top:1040px;width:1200px;height:622px;background:var(--grey-bg)}
.sec-title{left:0;width:1200px;text-align:center;font-size:34px}
.card{top:1181px;width:227px;height:216px;background:var(--white);border-radius:4px}
.card .ph{position:absolute;left:20px;top:20px;width:187px;height:140px;border-radius:3px}
.plus{width:52px;height:52px;border-radius:50%;background:var(--green-dark);color:var(--white);font-size:32px;display:flex;align-items:center;justify-content:center;top:1371px;font-weight:600}
.stars{top:1438px;width:227px;text-align:center;color:var(--star);font-size:17px;letter-spacing:4px}
.pname{top:1468px;width:227px;text-align:center;font-family:"Michroma",sans-serif;font-size:14px;line-height:22px;color:var(--ink);text-transform:uppercase}
.slide-btn{width:38px;height:38px;border-radius:50%;top:1298px;display:flex;align-items:center;justify-content:center;font-size:16px}

/* story */
.story{left:0;top:1662px;width:1200px;height:505px;background:radial-gradient(ellipse at 70% 40%,#1d9a1d,var(--green-deep) 75%)}
.story-photo{left:96px;top:1582px;width:500px;height:585px;border-radius:120px 120px 0 0;background:linear-gradient(180deg,#d9551f 0%,#c49279 25%,#5b5a58 55%,#3e3d3c 100%)}
.story-title{left:691px;top:1733px;font-size:34px;color:var(--white)}
.story-text{left:691px;top:1786px;width:420px;font-size:15px;line-height:25.7px;color:var(--white)}
.story-btn{left:692px;top:2038px;width:194px;height:55px;font-size:15px}

/* contact */
.contact-title{top:2247px}
.info{left:180px;display:flex;gap:26px}
.info .ic{width:54px;height:54px;border-radius:50%;background:#f1f1f1;box-shadow:0 2px 6px rgba(0,0,0,.08);display:flex;align-items:center;justify-content:center}
.info h4{font-family:"Michroma",sans-serif;font-weight:400;font-size:18px;color:var(--ink);margin-top:8px}
.info p{font-size:17px;line-height:23px;margin-top:6px;color:var(--ink)}
.form{left:576px;top:2327px;width:439px;height:443px;background:var(--white);box-shadow:0 4px 24px rgba(0,0,0,.08);padding:38px 46px}
.form h3{font-family:"Michroma",sans-serif;font-weight:400;font-size:20px;color:var(--ink);text-transform:uppercase}
.field{border-bottom:1.5px solid #444;font-size:15px;color:var(--ink);padding-bottom:12px}
.send{position:absolute;left:48px;top:355px;width:118px;height:42px;border-radius:21px;background:var(--green-dark);color:var(--white);font-family:"Michroma",sans-serif;font-size:15px;display:flex;align-items:center;justify-content:center}

/* footer */
.footer{left:0;top:2855px;width:1200px;height:387px;background:var(--footer);color:var(--white)}
.foot-brand{left:112px;top:2988px;display:flex;align-items:center;gap:12px;font-size:26px;font-weight:600;letter-spacing:1px;color:var(--white)}
.foot-brand .mark{width:40px;height:40px;border-radius:50%;background:var(--green)}
.fcol{top:2922px;color:var(--white)}
.fcol h5{font-family:"Michroma",sans-serif;font-weight:400;font-size:17px;text-transform:uppercase;margin-bottom:18px;color:var(--white)}
.fcol li{list-style:none;font-size:15px;line-height:30px;padding-left:5px;color:var(--white)}
.newsletter{left:823px;top:2966px;width:258px;height:38px;border:1px solid #888;border-radius:3px;display:flex;align-items:center;justify-content:space-between;padding:0 10px;font-size:14px;color:#999}
.fsocial{left:832px;top:3042px;display:flex;gap:12px}
.fsocial span{width:12px;height:12px;border-radius:50%;background:var(--white)}
.divider{left:100px;top:3155px;width:1000px;height:1px;background:#333}
.copy{left:0;width:1200px;top:3188px;text-align:center;font-size:15px;color:var(--white)}
</style>
</head>
<body>

<section class="hero abs">
  <div class="hero-photo abs" role="img" aria-label="Photo of a lumber warehouse with stacked timber on racks"></div>
  <div class="hero-shade abs"></div>
  <svg class="abs" style="left:0;top:0" width="1200" height="660" viewBox="0 0 1200 660">
    <polygon points="0,660 0,600 560,280 1200,0 1200,0 620,400 420,660" fill="#0a9a0a" opacity=".85"/>
  </svg>
  <div class="topbar abs"></div>
</section>

<div class="brand abs"><span class="brand-dot"></span>BRINDLEQUAY</div>

<div class="contact-item abs" style="left:452px">
  <svg width="40" height="40" viewBox="0 0 24 24" fill="none" stroke="#3ed13e" stroke-width="1.4"><path d="M5 3h4l2 5-3 2a11 11 0 0 0 6 6l2-3 5 2v4a2 2 0 0 1-2 2A17 17 0 0 1 3 5a2 2 0 0 1 2-2z"/></svg>
  <div><div class="label">Call Us</div><div class="value">555-014-2290</div></div>
</div>
<div class="contact-item abs" style="left:658px">
  <svg width="40" height="40" viewBox="0 0 24 24" fill="none" stroke="#3ed13e" stroke-width="1.4"><rect x="2" y="5" width="20" height="14"/><path d="M2 5l10 8 10-8"/></svg>
  <div><div class="label">Email</div><div class="value">Info@brindlequay.com</div></div>
</div>
<div class="contact-item abs" style="left:892px">
  <svg width="38" height="38" viewBox="0 0 24 24" fill="none" stroke="#3ed13e" stroke-width="1.4"><circle cx="12" cy="12" r="10"/><path d="M12 6v6l4 2"/></svg>
  <div><div class="label">Working Hours</div><div class="value">M-F 6am-6pm</div></div>
</div>

<nav class="nav abs">
  <a class="active">Home</a><a>About Us</a><a>POD Look Up</a><a>Products</a><a>Contact Us</a>
  <div class="search">Search
    <svg width="14" height="14" viewBox="0 0 24 24" fill="none" stroke="#0a8a0a" stroke-width="3"><circle cx="10" cy="10" r="7"/><path d="M15 15l6 6"/></svg>
  </div>
  <div class="socials"><span></span><span></span><span></span><span></span></div>
</nav>

<div class="hero-sub abs">Brindlequay Industries Co., Inc.</div>
<h1 class="hero-title abs display" style="color:#fff">Construction Supplies<br>&amp; Building Materials</h1>
<div class="hero-btn btn abs">Get Started</div>
<div class="dots abs"><span></span><span class="off"></span><span></span><span></span></div>

<div class="why-kicker abs">Why do business</div>
<h2 class="why-title abs display">With Brindlequay?</h2>
<p class="why-text abs">Lorem ipsum dolor sit amet, consectetur adipiscing elit, sed do eiusmod tempor incididunt ut labore et dolore magna aliqua.</p>
<div class="learn abs">Learn More</div>
<div class="arrows abs"><span style="color:#bbb">←</span><span style="color:var(--green)">→</span></div>

<div class="feature abs" style="left:394px">
  <svg width="68" height="68" viewBox="0 0 48 48" fill="none" stroke="#111" stroke-width="1.6"><rect x="14" y="18" width="20" height="16"/><path d="M14 18l10-6 10 6M24 12v22"/><path d="M4 40h10l8 2 14-6"/><circle cx="32" cy="10" r="5" stroke="#0a8a0a"/></svg>
  <h3>Service &amp; Relationship<br>Based Company</h3>
  <p>Lorem ipsum dolor sit amet, consectetur adipiscing elit, sed do eiusmod tempor incididunt ut labore et dolore magna aliqua.</p>
</div>
<div class="feature abs" style="left:654px">
  <svg width="84" height="68" viewBox="0 0 60 48" fill="none" stroke="#111" stroke-width="1.6"><rect x="6" y="12" width="30" height="22" fill="#9fd39f"/><path d="M36 18h10l8 9v7H36z"/><circle cx="16" cy="38" r="4"/><circle cx="46" cy="38" r="4"/><path d="M0 18h8M2 24h8"/></svg>
  <h3>Deliver Fast and<br>On Time</h3>
  <p>Lorem ipsum dolor sit amet, consectetur adipiscing elit, sed do eiusmod tempor incididunt ut labore et dolore magna aliqua.</p>
</div>
<div class="feature abs" style="left:912px">
  <svg width="68" height="68" viewBox="0 0 48 48" fill="none" stroke="#111" stroke-width="1.6"><path d="M4 14l16-8 16 8v18l-16 8-16-8z"/><path d="M4 14l16 8 16-8M20 22v18"/><rect x="30" y="24" width="14" height="18" fill="#9fd39f"/><path d="M33 30h8M33 34h8M33 38h8"/></svg>
  <h3>One Stop Shop With<br>Wide Range of Products</h3>
  <p>Lorem ipsum dolor sit amet, consectetur adipiscing elit, sed do eiusmod tempor incididunt ut labore et dolore magna aliqua.</p>
</div>

<section class="products abs"></section>
<h2 class="sec-title abs display" style="top:1098px">Our Products</h2>

<div class="slide-btn abs" style="left:39px;background:#e2e2e2;color:#111">‹</div>
<div class="slide-btn abs" style="left:1123px;background:var(--green-dark);color:#fff">›</div>

<div class="card abs" style="left:112px"><div class="ph" role="img" aria-label="Photo of a concrete block and bricks" style="background:linear-gradient(135deg,#e2e2e2,#c9a78f)"></div></div>
<div class="card abs" style="left:362px"><div class="ph" role="img" aria-label="Photo of a round concrete slab" style="background:linear-gradient(180deg,#fff,#d8d8d8 60%,#fff)"></div></div>
<div class="card abs" style="left:612px"><div class="ph" role="img" aria-label="Photo of stacked cement bags" style="background:linear-gradient(135deg,#e6d8c0,#8a5a3c)"></div></div>
<div class="card abs" style="left:861px"><div class="ph" role="img" aria-label="Photo of a corrugated metal drainage sheet" style="background:linear-gradient(180deg,#fff,#b8bcc2 60%,#fff)"></div></div>

<div class="plus abs" style="left:199px">+</div>
<div class="plus abs" style="left:449px">+</div>
<div class="plus abs" style="left:699px">+</div>
<div class="plus abs" style="left:948px">+</div>

<div class="stars abs" style="left:112px">★★★★★</div>
<div class="stars abs" style="left:362px">★★★★★</div>
<div class="stars abs" style="left:612px">★★★★★</div>
<div class="stars abs" style="left:861px">★★★★★</div>

<div class="pname abs" style="left:112px">Concrete Forming<br>Accessories</div>
<div class="pname abs" style="left:362px">Concrete Repair<br>Mortars</div>
<div class="pname abs" style="left:612px">Concrete<br>Reinforcement</div>
<div class="pname abs" style="left:861px">Waterproofing<br>Drainage</div>

<section class="story abs"></section>
<div class="story-photo abs" role="img" aria-label="Photo of a smiling construction worker in an orange hard hat and work jacket"></div>
<h2 class="story-title abs display" style="color:#fff">Our Story</h2>
<p class="story-text abs">Brindlequay is a family owned and operated company that has been in the business of selling construction supplies since 1991. For over 30 years we have provided small and large companies with our reliable products, ranging from bagged sand and concrete to rebar and wire mats. We specialize in the sale of concrete infrastructure materials, and we can fulfill your requirements for almost anything on your job site. Brindlequay has hundreds of reputable brands and over 20,000 products to choose from.</p>
<div class="story-btn btn abs">Learn More</div>

<h2 class="sec-title contact-title abs display">Contact Us</h2>

<div class="info abs" style="top:2388px">
  <div class="ic"><svg width="14" height="18" viewBox="0 0 24 30"><path d="M12 0a10 10 0 0 0-10 10c0 8 10 20 10 20s10-12 10-20A10 10 0 0 0 12 0zm0 14a4 4 0 1 1 0-8 4 4 0 0 1 0 8z" fill="#0a8a0a"/></svg></div>
  <div><h4>ADDRESS</h4><p>418 Harbor Mill Road<br>Westfield, NJ 07090</p></div>
</div>
<div class="info abs" style="top:2517px">
  <div class="ic"><svg width="16" height="16" viewBox="0 0 24 24"><path d="M5 2h4l2 5-3 2a11 11 0 0 0 6 6l2-3 5 2v4a2 2 0 0 1-2 2A18 18 0 0 1 3 4a2 2 0 0 1 2-2z" fill="#0a8a0a"/></svg></div>
  <div><h4>PHONE</h4><p>555-014-2290</p></div>
</div>
<div class="info abs" style="top:2633px">
  <div class="ic"><svg width="16" height="12" viewBox="0 0 24 18"><rect width="24" height="18" rx="2" fill="#0a8a0a"/><path d="M1 2l11 8 11-8" fill="none" stroke="#f1f1f1" stroke-width="2"/></svg></div>
  <div><h4>EMAIL</h4><p style="color:var(--green)">info@brindlequayindustries.com</p></div>
</div>

<div class="form abs">
  <h3>Send Message</h3>
  <div class="field" style="margin-top:34px">Full Name</div>
  <div class="field" style="margin-top:34px">Last Name</div>
  <div class="field" style="margin-top:40px">Address</div>
  <div class="field" style="margin-top:40px">Types Your Message</div>
  <div class="send">SEND</div>
</div>

<footer class="footer abs"></footer>
<div class="foot-brand abs"><span class="mark"></span>BRINDLEQUAY</div>

<div class="fcol abs" style="left:442px"><h5>Quick Link</h5><ul><li>Home</li><li>About Us</li><li>POD Look Up</li><li>Products</li><li>Contact Us</li></ul></div>
<div class="fcol abs" style="left:630px"><h5>Help Link</h5><ul><li>Terms&amp;condtions</li><li>Privacy Policy</li><li>About Us</li><li>Support</li></ul></div>
<div class="fcol abs" style="left:822px"><h5>Get Our Newsletter</h5></div>
<div class="newsletter abs">Enter Your Email
  <svg width="16" height="16" viewBox="0 0 24 24"><path d="M2 12L22 2 16 22l-4-8z" fill="#1fb81f"/></svg>
</div>
<div class="fsocial abs"><span></span><span></span><span></span><span></span></div>
<div class="divider abs"></div>
<div class="copy abs">©Copyrights 2022 Brindlequay Industries | &nbsp; All Rights Reserved</div>

</body>
</html>
```